I need a flyer made , the flyer can be one page or two pages or three pages . I will be posting this on Instagram and social media platforms. I am a luxury home builder , I am looking to hire a construction project manager . Below are some examples and ideas what can be on the flyer

We’re looking for a construction project manager who’s passionate about building luxury homes at the highest standards
We’re hiring construction project manager
* Experience 5+ years in residential project management with a strong portfolio of completed homes.
* location : Bergen County NJ
* excellent leadership skills, leads teams with confidence and clarity
* communicates seamlessly with architects , engineers, designers and clients
*knows how to manage budgets and timelines without compromising quality
*solves problems with a positive solution first mindset
* pays attention to every detail because in luxury the small things are the big things

Apply now , link in bio or DM to connect.

My logo is attached, my web site www.ridgelanebuilders.com
My style is modern but still warm and inviting. I like a clean classy look .
Updates

Please don’t add any images of chairs or people to the flyer , I do not want people on my flyer. Do not add standard images of offices and houses , we are luxury builders , we build homes over 2 million dollars. Keep a classy , simple modern look . High end .

You can add a white hard hat with my logo on it for a image , this is a suggestion does not have to be on my flyer ,

```html
<!DOCTYPE html>
<html lang="en">
<head>
<meta charset="utf-8">
<title>Ridgelane Builders – We Are Hiring</title>
<link rel="stylesheet" href="https://fonts.googleapis.com/css2?family=Anton&family=DM+Sans:wght@400;700&family=Lexend:wght@700;800&display=swap">
<style>
  :root {
    --paper: #ffffff;
    --ink: #0c0d0c;
    --night: #060606;
    --photo-light: #9a938c;
    --photo-mid: #4a4846;
    --photo-dark: #1c1b1a;
  }
  * { margin: 0; padding: 0; box-sizing: border-box; }
  html, body { width: 927px; height: 1200px; overflow: hidden; background: var(--paper); }
  .flyer { position: relative; width: 927px; height: 1200px; background: var(--paper); overflow: hidden; }
  .hero-photo {
    position: absolute; left: 51px; top: 67px; width: 808px; height: 617px;
    background:
      linear-gradient(180deg, rgba(0,0,0,0) 60%, var(--night) 100%),
      linear-gradient(90deg, var(--photo-mid) 0%, var(--photo-dark) 22%, var(--photo-light) 48%, var(--photo-mid) 72%, var(--photo-dark) 100%);
  }
  .dark-base {
    position: absolute; left: 51px; top: 684px; width: 808px; height: 428px;
    background: radial-gradient(ellipse at 50% 40%, #151515 0%, var(--night) 80%);
  }
  .house { position: absolute; left: 0; top: 0; }
  .brand {
    position: absolute; left: 221px; width: 491px; top: 212px; text-align: center;
    font-family: "DM Sans", sans-serif; font-weight: 700; font-size: 26px;
    letter-spacing: 3px; color: var(--ink); text-transform: uppercase; white-space: nowrap;
  }
  .headline {
    position: absolute; left: 221px; width: 491px; text-align: center;
    font-family: "Anton", sans-serif; font-weight: 400; color: var(--ink); line-height: 1; white-space: nowrap;
  }
  .headline.top { top: 287px; font-size: 146px; letter-spacing: 1px; }
  .headline.bottom { top: 431px; font-size: 146px; letter-spacing: -1px; }
  .role-band {
    position: absolute; left: 264px; top: 575px; width: 401px; height: 64px;
    background: var(--ink); color: var(--paper); text-align: center;
    font-family: "Lexend", sans-serif; font-weight: 800; font-size: 24px; line-height: 27px;
    padding-top: 5px; letter-spacing: 0.5px; white-space: nowrap;
  }
  .location {
    position: absolute; left: 221px; width: 491px; top: 640px; text-align: center;
    font-family: "Lexend", sans-serif; font-weight: 700; font-size: 30px; line-height: 40px;
    color: var(--ink); white-space: nowrap; letter-spacing: -0.3px;
  }
  .intro {
    position: absolute; left: 240px; width: 454px; top: 694px; text-align: center;
    font-family: "DM Sans", sans-serif; font-weight: 700; font-size: 20.5px; line-height: 28.5px;
    color: var(--paper); letter-spacing: -0.3px;
  }
  .requirements {
    position: absolute; left: 225px; top: 813px; width: 479px; height: 196px;
    background: var(--paper); border-radius: 16px; padding: 14px 0 0 30px;
  }
  .requirements h2 {
    font-family: "Lexend", sans-serif; font-weight: 800; font-size: 25px; color: var(--ink);
    line-height: 34px; white-space: nowrap;
  }
  .requirements ul {
    margin-top: 8px; padding-left: 23px;
    font-family: "DM Sans", sans-serif; font-size: 13.5px; line-height: 21.9px; color: var(--ink);
  }
  .announce { position: absolute; left: 603px; top: 782px; }
  .apply {
    position: absolute; left: 225px; top: 1022px; width: 478px; height: 51px;
    border: 3px solid var(--paper); border-radius: 12px; background: var(--night); overflow: hidden;
    display: flex;
  }
  .apply-label {
    width: 214px; background: var(--paper); border-radius: 0 12px 12px 0;
    font-family: "Lexend", sans-serif; font-weight: 700; font-size: 20px; color: var(--ink);
    display: flex; align-items: center; justify-content: center; letter-spacing: -0.5px; white-space: nowrap;
  }
  .apply-contact {
    flex: 1; color: var(--paper); text-align: center; font-family: "DM Sans", sans-serif;
    font-size: 14px; line-height: 17px; padding-top: 5px; white-space: nowrap;
  }
  .apply-contact strong { font-weight: 700; }
</style>
</head>
<body>
<main class="flyer">
  <div class="hero-photo" role="img" aria-label="Luxury bathroom interior with dark stone wall, round wood-framed mirror and recessed ceiling lights"></div>
  <div class="dark-base"></div>

  <svg class="house" width="927" height="700" viewBox="0 0 927 700" aria-hidden="true">
    <polyline points="531,158 571,128 807,285" fill="none" stroke="#ffffff" stroke-width="7" stroke-linecap="round" stroke-linejoin="round"/>
    <polyline points="300,230 300,158 347,158 347,215" fill="none" stroke="#ffffff" stroke-width="7" stroke-linejoin="round"/>
    <polygon points="465,121 712,280 712,683 221,683 221,280" fill="#ffffff" stroke="#ffffff" stroke-width="8" stroke-linejoin="round"/>
    <line x1="215" y1="286" x2="465" y2="121" stroke="#ffffff" stroke-width="9" stroke-linecap="round"/>
    <line x1="715" y1="286" x2="465" y2="121" stroke="#ffffff" stroke-width="9" stroke-linecap="round"/>
  </svg>

  <div class="brand">Ridgelane Builders</div>
  <h1>
    <span class="headline top">WE ARE</span>
    <span class="headline bottom">HIRING</span>
  </h1>
  <div class="role-band">CONSTRUCTION<br>PROJECT MANAGER</div>
  <div class="location">Bergen County, NJ</div>

  <p class="intro">We’re looking for a Residential Project Manager with 5+ years experience and a strong portfolio of completed homes.</p>

  <section class="requirements">
    <h2>REQUIREMENTS:</h2>
    <ul>
      <li>Lead teams with confidence</li>
      <li>Lead teams with confidence</li>
      <li>Communicate with architects, designers &amp; clients</li>
      <li>Manage budgets &amp; timelines without sacrificing quality</li>
      <li>Solve problems with a solution-first mindset</li>
      <li>Obsess over the details — in luxury, they matter most</li>
    </ul>
  </section>

  <svg class="announce" width="122" height="122" viewBox="0 0 122 122" aria-hidden="true">
    <circle cx="61" cy="61" r="60" fill="#ffffff"/>
    <circle cx="61" cy="61" r="50" fill="#0c0d0c"/>
    <g fill="#ffffff" stroke="#ffffff" stroke-linecap="round">
      <polygon points="48,72 63,40 80,68" stroke-width="2" stroke-linejoin="round"/>
      <circle cx="82" cy="64" r="7" stroke="none"/>
      <line x1="64" y1="73" x2="58" y2="86" stroke-width="3"/>
      <line x1="56" y1="79" x2="66" y2="81" stroke-width="2.5" fill="none"/>
      <line x1="37" y1="50" x2="42" y2="53" stroke-width="2.5"/>
      <line x1="47" y1="38" x2="50" y2="44" stroke-width="2.5"/>
      <line x1="35" y1="63" x2="41" y2="62" stroke-width="2.5"/>
    </g>
  </svg>

  <div class="apply">
    <div class="apply-label">Apply Now</div>
    <div class="apply-contact">Link in bio or DM to connect.<br><strong>info@ridgelanebuilders.com</strong></div>
  </div>
</main>
</body>
</html>
```